Marlene Business Card

My wife is going to start her own business with renting holiday appartments to tourists. She needs a design for a new business card... and a new web site.
Look at Roomvesta "Ruhezeit am Birkenteich"

Target Market(s)

Give business card to prospects at any situation

Contact Information for Business Card

not sure what this means

Font styles to use
Script

Colors
fec41a
fee18a

Requirements
Must have
• My wife's handwriting is difficult to read:
Entspannen - Loslassen - Auftanken
Marlene & der Birkenteich
Urlaub an einem besonderen Ort
Marlene Brökel
Gartenpfad 7
17489 Alt Medow
info@marlene-broekel.de
www.birkenteich.net
Nice to have
• Beige background
Font like handwriting

```html
<!DOCTYPE html>
<html lang="de">
<head>
<meta charset="utf-8">
<title>Marlene &amp; der Birkenteich – Visitenkarte</title>
<link rel="stylesheet" href="https://fonts.googleapis.com/css2?family=Pinyon+Script&family=Playball&display=swap">
<style>
  :root {
    --page-beige: #ead6bc;
    --card-yellow: #fec41a;
    --ink: #0d0a05;
  }
  * { margin: 0; padding: 0; box-sizing: border-box; }
  html, body {
    width: 1200px;
    height: 908px;
    overflow: hidden;
    background: var(--page-beige);
  }
  .business-card {
    position: absolute;
    left: 244px;
    top: 252px;
    width: 677px;
    height: 403px;
    background: var(--card-yellow);
    color: var(--ink);
    font-family: "Pinyon Script", cursive;
  }
  .business-card > * { position: absolute; line-height: 1; white-space: nowrap; }
  .tagline {
    left: 0; right: 0; top: 62px;
    text-align: center;
    font-size: 37px;
  }
  .tagline-rule {
    left: 71px; top: 131px;
    width: 526px; height: 4px;
    background: var(--ink);
  }
  .business-name {
    left: 0; width: 645px; top: 165px;
    text-align: center;
    font-size: 46px;
  }
  .business-claim {
    left: 0; width: 645px; top: 213px;
    text-align: center;
    font-size: 28px;
  }
  .address-block {
    right: 366px; top: 284px;
    text-align: right;
  }
  .owner-name {
    font-family: "Playball", cursive;
    font-size: 22px;
    display: block;
    margin-bottom: 6px;
  }
  .address-line {
    display: block;
    font-size: 21px;
    line-height: 26px;
  }
  .contact-divider {
    left: 338px; top: 314px;
    width: 2px; height: 46px;
    background: var(--ink);
  }
  .contact-block {
    left: 365px; top: 306px;
  }
  .contact-line {
    display: block;
    font-size: 21px;
    line-height: 26px;
  }
  .contact-line.web { padding-left: 4px; }
</style>
</head>
<body>
  <section class="business-card">
    <p class="tagline">Entspannen - Loslassen - Auftanken</p>
    <div class="tagline-rule"></div>
    <h1 class="business-name" style="font-weight:400">Marlene &amp; der Birkenteich</h1>
    <p class="business-claim">Urlaub an einem besonderen Ort</p>
    <address class="address-block" style="font-style:normal">
      <span class="owner-name">Marlene Brökel</span>
      <span class="address-line">Gartenpfad 7</span>
      <span class="address-line">17489 Alt Medow</span>
    </address>
    <div class="contact-divider"></div>
    <div class="contact-block">
      <span class="contact-line">info@marlene-broekel.de</span>
      <span class="contact-line web">www.birkenteich.net</span>
    </div>
  </section>
</body>
</html>
```